Post card

I want an educational customer postcard with our logo, email, and contact number. We are a residential foundation inspection & repair company here in Los Angeles. We provide foundation repair, earthquake retrofitting, and reinforcement.
Our number is 323-555-0148.
Email info@bramblecrestworks.com
Our license number is #2839165

OUR GOAL
Our primary objective is to empower clients with comprehensive knowledge about foundation issues and earthquake retrofitting. By educating them on the potential risks associated with foundation problems and the importance of earthquake retrofitting, we aim to equip homeowners with the necessary information to make informed decisions about safeguarding their properties. Highlighting the benefits of having their houses properly bolted not only enhances structural integrity but also provides peace of mind during seismic events, ensuring the safety and security of their homes and loved ones.

```html
<!DOCTYPE html>
<html lang="en">
<head>
<meta charset="utf-8">
<title>Bramblecrest Works – Postcard</title>
<link rel="stylesheet" href="https://fonts.googleapis.com/css2?family=Montserrat:wght@500;600;700;800&display=swap">
<style>
  :root{
    --blue:#1460f0;
    --red:#cf1020;
    --dark:#262626;
    --white:#ffffff;
    --ink:#161616;
    --page:#ececec;
    --photo-b:#d9763a;
  }
  *{box-sizing:border-box;margin:0;padding:0}
  html,body{width:918px;height:1200px;overflow:hidden;background:var(--page)}
  body{font-family:"Montserrat",sans-serif;color:var(--ink);position:relative}
  .card{position:absolute;left:59px;width:800px;height:566px;background:var(--white);overflow:hidden;box-shadow:0 6px 16px rgba(0,0,0,.18)}
  .card--front{top:22px}
  .card--back{top:612px}
  .card-art{position:absolute;inset:0;width:100%;height:100%}
  .abs{position:absolute}
  .brand{display:flex;align-items:center;gap:9px}
  .brand-mark{width:30px;height:30px;background:var(--blue);flex:none}
  .brand-name{font-weight:800;font-size:21px;line-height:22px;color:var(--blue);text-transform:uppercase;letter-spacing:.5px}
  .brand--light .brand-mark{background:var(--white)}
  .brand--light .brand-name{color:var(--white);font-size:19px;line-height:20px}
  .intro{left:48px;top:108px;font-size:16px;line-height:20px;font-weight:500}
  .contact-title{left:18px;top:361px;font-size:27px;font-weight:800;color:var(--white);letter-spacing:.5px}
  .contact-line{left:44px;display:flex;align-items:center;gap:14px;font-size:16px;color:var(--white);font-weight:500}
  .contact-line svg{width:16px;height:16px}
  .contact-line--phone{top:415px}
  .contact-line--mail{top:442px}
  .license-label{left:60px;top:487px;font-size:18px;font-weight:500}
  .license-number{left:58px;top:507px;font-size:48px;font-weight:800;color:var(--red);letter-spacing:1px}
  .goal-title{left:22px;top:36px;font-size:28px;font-weight:800;color:var(--white);letter-spacing:.5px}
  .goal-text{left:40px;top:106px;font-size:15.6px;line-height:20.3px;font-weight:500;color:var(--white);text-transform:uppercase}
</style>
</head>
<body>

<section class="card card--front" aria-label="Postcard front">
  <svg class="card-art" viewBox="0 0 752 532" preserveAspectRatio="none">
    <defs>
      <linearGradient id="photoTone" x1="0" y1="0" x2="1" y2="1">
        <stop offset="0" stop-color="#d8d4cc"/>
        <stop offset=".5" stop-color="var(--photo-b)"/>
        <stop offset="1" stop-color="#6e5a45"/>
      </linearGradient>
    </defs>
    <path role="img" aria-label="Photo of a worker in an orange hard hat repairing a house foundation wall" d="M290,0 H752 V532 H520 C400,460 300,320 290,0 Z" fill="url(#photoTone)"/>
    <path d="M262,0 H290 C300,320 400,460 520,532 H470 C350,450 272,300 262,0 Z" fill="var(--red)"/>
    <path d="M300,360 C360,450 420,505 470,532 H440 C380,500 330,450 290,380 Z" fill="var(--white)"/>
    <path d="M290,380 C330,450 380,500 440,532 H390 C340,500 300,450 275,395 Z" fill="var(--blue)"/>
    <rect role="img" aria-label="Seismic wave band" x="0" y="300" width="250" height="5" fill="var(--blue)"/>
    <rect x="0" y="380" width="345" height="68" fill="var(--red)"/>
    <path d="M0,332 H245 L265,332 L290,380 H0 Z" fill="var(--dark)"/>
    <path d="M0,332 H245 L225,380 H0 Z" fill="var(--blue)"/>
  </svg>

  <div class="abs brand" style="left:37px;top:30px">
    <span class="brand-mark"></span>
    <span class="brand-name">Bramblecrest<br>Works</span>
  </div>

  <p class="abs intro">We are a residential<br>foundation inspection<br>&amp; repair company<br>here in Los Angeles.<br>We provide foundation<br>repair, earthquake<br>retrofitting, and<br>reinforcement.</p>

  <h2 class="abs contact-title">CONTACT US</h2>
  <div class="abs contact-line contact-line--phone">
    <svg viewBox="0 0 16 16"><path d="M3 1.5 L6 1.5 L7 5 L5.2 6.3 C6 8.3 7.7 10 9.7 10.8 L11 9 L14.5 10 L14.5 13 C14.5 14 13.6 14.6 12.6 14.5 C6.8 13.8 2.2 9.2 1.5 3.4 C1.4 2.4 2 1.5 3 1.5 Z" fill="var(--white)"/></svg>
    <span>323-555-0148</span>
  </div>
  <div class="abs contact-line contact-line--mail">
    <svg viewBox="0 0 16 16"><rect x="1" y="3" width="14" height="10" fill="var(--white)"/><path d="M1 3 L8 9 L15 3" fill="none" stroke="var(--red)" stroke-width="1.4"/></svg>
    <span>info@bramblecrestworks.com</span>
  </div>

  <p class="abs license-label">Our license number is</p>
  <p class="abs license-number">2839165</p>
</section>

<section class="card card--back" aria-label="Postcard back">
  <svg class="card-art" viewBox="0 0 752 532" preserveAspectRatio="none">
    <path d="M0,0 H495 C470,250 430,420 310,532 H0 Z" fill="var(--blue)"/>
    <path d="M468,265 C450,400 400,480 340,532 H390 C440,480 466,390 468,265 Z" fill="var(--red)"/>
    <path d="M0,25 H222 L196,75 H0 Z" fill="var(--red)"/>
    <rect x="598" y="58" width="122" height="134" fill="none" stroke="var(--ink)" stroke-width="1.5"/>
    <g stroke="var(--ink)" stroke-width="1.3">
      <line x1="525" y1="255" x2="720" y2="255"/>
      <line x1="508" y1="295" x2="720" y2="295"/>
      <line x1="498" y1="335" x2="720" y2="335"/>
      <line x1="485" y1="378" x2="720" y2="378"/>
      <line x1="470" y1="420" x2="720" y2="420"/>
    </g>
    <rect role="img" aria-label="Seismic wave band" x="440" y="492" width="312" height="5" fill="var(--blue)"/>
  </svg>

  <h2 class="abs goal-title">OUR GOAL</h2>
  <p class="abs goal-text">Our primary objective is to empower<br>clients with comprehensive knowledge<br>about foundation issues and<br>earthquake retrofitting. By educating<br>them on the potential risks associated<br>with foundation problems and the<br>importance of earthquake retrofitting,<br>we aim to equip homeowners with the<br>necessary information to make<br>informed decisions about<br>safeguarding their properties<br>highlighting the benefits of having<br>their houses properly bolted<br>not only enhances structural<br>integrity but also provides peace<br>of mind during seismic events,<br>ensuring the safety and security<br>of their homes and loved ones.</p>

  <div class="abs brand brand--light" style="left:50px;top:494px">
    <span class="brand-mark"></span>
    <span class="brand-name">Bramblecrest<br>Works</span>
  </div>
</section>

</body>
</html>
```